New Interfaces

The software open with 3 open tabs, you can see the interfaces following this steps:

Brindle:
Select tab "Brindle" and click on "Brindle" in menu on the top.

KPI :
Select tab "KPI" and click on go button.

Report:
Select tab "Report" and Click on go button.

Current software: http://volteq.vextal-example.com/volteq_developers/default.aspx

user: sample_guest
pass: plinkaa

......

About the company

The VexTal is a technology company that provides planning, optimization services and software to develop the market for telecom operators.

The Product

Volteq is a web management and optimization tool for mobile networks.

The project

To always offer the best experience of usability and comfort for our customers, we are remodeling our software. The goal is to have agile, modern and with special attention to usability interfaces.

user: sample_guest
pass: plinkaa

Hi! We are analyzing all interfaces, we send news soon. Thank you!

Target Market(s)

Telecommunications Engineers.

Industry/Entity Type

Software

Font styles to use
Sans Serif

Requirements
Nice to have
• Attention for usability and good concept.
Should not have
• Many colors.

```html
<!DOCTYPE html>
<html lang="en">
<head>
<meta charset="utf-8">
<title>VexTal – Volteq Interface</title>
<link href="https://fonts.googleapis.com/css2?family=Open+Sans:wght@400;600;700&display=swap" rel="stylesheet">
<style>
:root{
  --navy:#0e4c86;
  --orange:#e8812f;
  --peach:#fde3cc;
  --row-peach:#fbd3b0;
  --sky:#b9dcf5;
  --row-sky:#a8d5f3;
  --grey:#e4e4e4;
  --grey-dark:#8f8f8f;
  --page:#f1f1f1;
  --ink:#333;
}
*{box-sizing:border-box;margin:0;padding:0}
html,body{width:951px;height:1200px;overflow:hidden}
body{font-family:"Open Sans",Arial,sans-serif;color:var(--ink);background:var(--page);position:relative;font-size:10px}
.topbar{position:absolute;left:0;top:0;width:951px;height:40px;background:var(--navy);display:flex;align-items:center}
.search{margin-left:10px;width:198px;height:19px;background:#fff;position:relative}
.search-btn{position:absolute;right:0;top:0;width:20px;height:19px;background:var(--orange)}
.mainnav{display:flex;margin-left:12px;height:40px}
.mainnav a{color:#fff;text-decoration:none;font-size:8px;display:flex;align-items:center;padding:0 6px;border-right:1px solid #2a6198;gap:3px;white-space:nowrap}
.mainnav a svg{width:8px;height:8px}
.logoff{position:absolute;right:0;top:0;width:51px;height:40px;background:var(--orange);color:#fff;font-size:10px;display:flex;align-items:center;justify-content:center}
.sidebar{position:absolute;left:0;top:40px;width:208px;height:1086px;background:#fff;border-right:2px solid #e2e2e2}
.treemode{display:flex;align-items:center;height:22px;padding-left:10px;font-size:9px;color:#555}
.today{background:var(--orange);color:#fff;font-size:8px;padding:1px 10px;margin-left:10px}
.notes{margin-left:auto;margin-right:14px;font-size:8px;color:#888}
.views{display:flex;gap:8px;padding-left:15px;font-size:9.5px;margin-top:4px}
.views .on{color:var(--navy)}
.brand{margin:14px 0 0 42px;font-size:30px;font-weight:700;color:var(--navy);letter-spacing:-0.5px}
.group{margin:14px 0 0 16px;width:179px;height:24px;background:var(--navy);color:#fff;display:flex;align-items:center;font-size:9.5px;gap:8px;padding-left:6px}
.group .ico{width:10px;height:10px;border:1px solid #fff}
.tree{list-style:none;font-size:9.5px;color:#555}
.tree li{display:flex;align-items:center;gap:8px}
.box{width:8px;height:8px;border:1px solid #888;display:inline-block;position:relative;flex:none}
.box::before{content:"";position:absolute;left:1px;right:1px;top:3px;height:1px;background:#888}
.box.plus::after{content:"";position:absolute;top:1px;bottom:1px;left:3px;width:1px;background:#888}
.vendor{font-size:7.5px;color:#111}
.vend-mark{width:10px;height:10px;background:#b4b4b4;border-radius:50%;flex:none}
.tabs{position:absolute;left:210px;top:40px;width:741px;height:36px;background:#e6e6e6;display:flex}
.tab{height:36px;display:flex;align-items:center;padding-left:12px;font-size:10px;justify-content:space-between;padding-right:10px}
.tab.active{background:#fff;color:var(--navy);width:158px}
.tab.idle{width:92px;color:#777;background:#dcdcdc}
.x{color:var(--navy);font-weight:700}
.panel-head{position:absolute;left:218px;width:723px;height:32px;background:var(--sky);display:flex;align-items:center;font-size:12px;color:#444}
.panel-head .ctl{width:30px;padding-left:7px;color:var(--navy);font-weight:700;font-size:12px}
.panel-head .sep{border-left:1px solid #fff;height:32px;margin:0 22px 0 28px}
.subtabs{position:absolute;left:218px;top:124px;width:723px;height:34px;background:var(--peach);display:flex;align-items:center;font-size:10.5px;color:#555}
.subtabs .on{background:var(--orange);color:#fff;height:34px;width:174px;display:flex;align-items:center;justify-content:center;font-size:12px;font-weight:600}
.subtabs span{margin-left:15px;margin-right:8px}
.form{position:absolute;left:218px;top:158px;width:723px;height:214px;background:#fff}
.field{position:absolute;font-size:10px;color:#444}
.input{position:absolute;width:202px;height:28px;border:1px solid #dcdcdc;background:#fff}
.yn{position:absolute;width:70px;height:27px;display:flex;align-items:center;justify-content:center;font-size:11px;border:1px solid #ddd}
.toolbar{position:absolute;left:218px;top:432px;width:723px;height:32px;background:var(--peach);display:flex;align-items:center}
.gbtn{background:var(--grey-dark);color:#fff;font-size:7.5px;height:24px;display:flex;align-items:center;justify-content:center;margin-left:6px}
.obtn{background:var(--orange);color:#fff;font-size:8px;height:24px;width:72px;display:flex;align-items:center;justify-content:center}
.bar{position:absolute;left:226px;width:708px;height:17px;background:var(--grey);font-size:8.5px;padding-left:10px;display:flex;align-items:center;color:#444}
.caption{position:absolute;left:226px;top:517px;width:708px;text-align:center;font-size:8.5px;color:#444}
.tickets{position:absolute;left:226px;top:534px;width:708px;border-collapse:collapse;font-size:8.5px;table-layout:fixed}
.tickets th{background:var(--navy);color:#fff;font-weight:600;height:24px;font-size:9px;border-left:1px solid #2d6aa3}
.tickets td{height:32.25px;text-align:center;color:#555;font-size:8px;line-height:1.4;border-left:1px solid rgba(255,255,255,.5)}
.tickets tr:nth-child(odd) td{background:var(--row-peach)}
.tickets tr:nth-child(even) td{background:var(--row-sky)}
.tickets .id{text-align:left;padding-left:4px}
.tickets .id i{display:inline-block;width:9px;height:9px;background:#fff;border-radius:2px;vertical-align:middle;margin-right:10px}
.tickets .id u{color:var(--navy);font-size:9px}
.pager{position:absolute;left:226px;top:948px;width:708px;height:30px;background:var(--grey);font-size:9px;display:flex;align-items:center;padding-left:13px;gap:7px;color:#555}
.bulk{position:absolute;left:226px;top:992px;width:708px;height:50px;background:#fff;border:1px solid #ccc;display:flex;align-items:center}
.check{width:12px;height:12px;border:1px solid #bbb;margin-left:14px;margin-right:8px}
.select{height:15px;border:1px solid #bbb;font-size:7.5px;display:flex;align-items:center;padding-left:5px;position:relative;color:#555}
.select::after{content:"";position:absolute;right:0;top:-1px;width:11px;height:15px;background:var(--orange)}
.go{width:40px;height:20px;background:var(--navy);color:#fff;font-size:9px;display:flex;align-items:center;justify-content:center;margin-left:15px}
.legend{position:absolute;left:226px;top:1046px;display:flex;gap:2px}
.legend span{width:89px;height:13px;font-size:9px;display:flex;align-items:center;justify-content:center;color:#333}
.chartbar{position:absolute;left:226px;top:1073px;width:708px;height:17px;background:#d9d9d9;display:flex;align-items:center;font-size:7.5px;color:var(--navy)}
.chartbar .pill{background:#eee;color:#444;padding:1px 5px;margin:0 4px}
.chartbox{position:absolute;left:226px;top:1090px;width:708px;height:32px;background:#fff;border:1px solid #ccc}
.footer{position:absolute;left:0;top:1126px;width:951px;height:74px;background:var(--navy)}
.flinks{display:flex;justify-content:center;gap:14px;color:#fff;font-size:11px;padding-top:13px;padding-right:50px}
.frule{height:1px;background:#3a6fa2;margin-top:10px}
.copy{position:absolute;left:101px;top:50px;color:#fff;font-size:9.5px}
.social{position:absolute;left:772px;top:46px;display:flex;gap:9px}
.social i{width:15px;height:15px;border-radius:50%;background:#fff;display:block}
.tag{position:absolute;right:14px;top:52px;color:#fff;font-size:10px}
</style>
</head>
<body>
<header class="topbar">
  <div class="search"><div class="search-btn"></div></div>
  <nav class="mainnav">
    <a><svg viewBox="0 0 8 8"><circle cx="4" cy="4" r="3.2" fill="#fff"/></svg>Configuration</a>
    <a><svg viewBox="0 0 8 8"><circle cx="4" cy="4" r="3.2" fill="#fff"/></svg>Statistics</a>
    <a><svg viewBox="0 0 8 8"><circle cx="4" cy="4" r="3.2" fill="#fff"/></svg>Planned Network</a>
    <a><svg viewBox="0 0 8 8"><circle cx="4" cy="4" r="3.2" fill="#fff"/></svg>Main KPIs</a>
    <a><svg viewBox="0 0 8 8"><rect x="1" y="0.5" width="6" height="7" fill="#fff"/></svg>Reports</a>
    <a><svg viewBox="0 0 8 8"><rect x="0.5" y="1" width="7" height="6" fill="#fff"/></svg>Brindle</a>
    <a><svg viewBox="0 0 8 8"><circle cx="4" cy="4" r="3.2" fill="#fff"/></svg>Workorders</a>
    <a><svg viewBox="0 0 8 8"><circle cx="4" cy="4" r="3" fill="none" stroke="#fff" stroke-width="1.4"/></svg>Support</a>
    <a><svg viewBox="0 0 8 8"><circle cx="4" cy="4" r="3.2" fill="#fff"/></svg>Custom</a>
    <a><svg viewBox="0 0 8 8"><circle cx="4" cy="4" r="3" fill="none" stroke="#fff" stroke-width="1.4"/></svg>Myview</a>
    <a style="border:0">? Help</a>
  </nav>
  <div class="logoff">Logoff</div>
</header>

<aside class="sidebar">
  <div class="treemode">Tree Mode: <span class="today">Today</span><span class="notes">Notes ▯</span></div>
  <div class="views"><span class="on">TreeView</span>|<span>Workspaces</span>|<span>Brindle</span></div>
  <div class="brand">VexTal</div>
  <div class="group"><span class="box" style="border-color:#fff"></span><span class="ico"></span>Real Network</div>
  <ul class="tree" style="margin:5px 0 0 46px">
    <li style="height:24px"><span class="box"></span>Tessara</li>
  </ul>
  <ul class="tree" style="margin:0 0 0 65px">
    <li style="height:22px"><span class="box plus"></span>2G</li>
    <li style="height:22px"><span class="box plus"></span>3G</li>
    <li style="height:22px"><span class="box plus"></span>LTE</li>
    <li style="height:22px"><span class="box plus"></span>Core Ps</li>
    <li style="height:22px"><span class="box plus"></span>SAE - GW</li>
  </ul>
  <ul class="tree" style="margin:4px 0 0 45px">
    <li style="height:12px"><span class="box plus"></span><span class="vend-mark"></span><span class="vendor">KORVANE</span></li>
    <li style="height:12px"><span class="box plus"></span><span class="vend-mark"></span><span class="vendor">BELMARK</span></li>
    <li style="height:12px"><span class="box plus"></span><span class="vend-mark"></span><span class="vendor">QIRO</span></li>
    <li style="height:12px"><span class="box plus"></span><span class="vend-mark"></span><span class="vendor">STELLUX</span></li>
    <li style="height:12px"><span class="box plus"></span><span class="vend-mark"></span><span class="vendor">MULTIVENDOR</span></li>
    <li style="height:12px"><span class="box plus"></span><span class="vend-mark"></span><span class="vendor">ORTANIS</span></li>
  </ul>
  <div class="group" style="margin-top:14px"><span class="box" style="border-color:#fff"></span><span class="ico"></span>Planned Network</div>
  <ul class="tree" style="margin:6px 0 0 46px">
    <li style="height:18px"><span class="box plus"></span><span class="box" style="border-color:#777"></span>Public Network</li>
    <li style="height:18px"><span class="box plus"></span><span class="box" style="border-color:#777"></span>Private Network</li>
  </ul>
</aside>

<div class="tabs">
  <div class="tab active">New Tab <span class="x">✖</span></div>
  <div class="tab idle">Newtab <span style="font-weight:700;color:#777">+</span></div>
</div>

<div class="panel-head" style="top:88px"><span class="ctl">✖ +</span><span style="margin-left:16px">Account Preferences</span><span class="sep"></span>Save</div>
<div class="subtabs"><div class="on">User Preferences</div><span>Chart Prefernces</span><span>Interface Prefernces</span></div>
<section class="form">
  <span class="field" style="left:21px;top:30px">Receive update emails:</span><div class="input" style="left:139px;top:24px"></div>
  <span class="field" style="left:21px;top:75px">Phone:</span><div class="input" style="left:139px;top:68px"></div>
  <span class="field" style="left:21px;top:119px">Old Password:</span><div class="input" style="left:139px;top:112px"></div>
  <span class="field" style="left:21px;top:163px">Repeat Password:</span><div class="input" style="left:139px;top:156px"></div>
  <span class="field" style="left:380px;top:30px">Full Name:</span><div class="input" style="left:499px;top:24px"></div>
  <span class="field" style="left:380px;top:75px">E-mail:</span><div class="input" style="left:499px;top:68px"></div>
  <span class="field" style="left:380px;top:119px">New Password:</span><div class="input" style="left:499px;top:112px"></div>
  <span class="field" style="left:380px;top:163px">Receive update emails:</span>
  <div class="yn" style="left:499px;top:157px;background:#fff">Yes</div>
  <div class="yn" style="left:573px;top:157px;background:var(--navy);color:#fff;border-color:var(--navy)">No</div>
</section>

<div class="panel-head" style="top:396px"><span class="ctl">✖ +</span><span style="margin-left:16px">Trouble Tickets (TT)</span></div>
<div class="toolbar">
  <div class="gbtn" style="width:122px">USER PREFERENCES</div>
  <div class="gbtn" style="width:122px;margin-left:2px">SHOW MONITORED</div>
  <span style="font-size:8px;margin-left:27px;color:#444">Text or ID</span>
  <div style="width:122px;height:24px;background:#fff;margin-left:4px"></div>
  <div class="obtn" style="margin-left:3px">SHOW IT</div>
</div>
<div class="bar" style="top:474px">SELECTED IT</div>
<div class="bar" style="top:495px">SEARCH RESULT</div>
<div class="caption">FILTER RESULT</div>

<table class="tickets">
  <colgroup><col style="width:50px"><col style="width:26px"><col style="width:66px"><col style="width:42px"><col style="width:115px"><col style="width:81px"><col style="width:141px"><col style="width:103px"><col style="width:84px"></colgroup>
  <thead><tr><th>ID</th><th>N</th><th>PRIORITY</th><th>DAYS</th><th>STATUS</th><th>PROBLEM ID</th><th>DESCRIPTION</th><th>UPDATED</th><th>OPENED BY</th></tr></thead>
  <tbody>
    <tr><td class="id"><i></i><u>1592</u></td><td>2</td><td>None</td><td>7</td><td>Feedback<br>([VexTal] Support_team)</td><td>New Feature<br>Request</td><td>Editor os estilos do treeview do<br>Volteq atual co..</td><td>2014 - 12 - 03 15:59:54</td><td>[VexTal]<br>Support_team</td></tr>
    <tr><td class="id"><i></i><u>1592</u></td><td>2</td><td>None</td><td>7</td><td>Feedback<br>([VexTal] Support_team)</td><td>New Feature<br>Request</td><td>Editor os estilos do treeview do<br>Volteq atual co..</td><td>2014 - 12 - 03 15:59:54</td><td>[VexTal]<br>Support_team</td></tr>
    <tr><td class="id"><i></i><u>1592</u></td><td>2</td><td>None</td><td>7</td><td>Feedback<br>([VexTal] Support_team)</td><td>New Feature<br>Request</td><td>Editor os estilos do treeview do<br>Volteq atual co..</td><td>2014 - 12 - 03 15:59:54</td><td>[VexTal]<br>Support_team</td></tr>
    <tr><td class="id"><i></i><u>1592</u></td><td>2</td><td>None</td><td>7</td><td>Feedback<br>([VexTal] Support_team)</td><td>New Feature<br>Request</td><td>Editor os estilos do treeview do<br>Volteq atual co..</td><td>2014 - 12 - 03 15:59:54</td><td>[VexTal]<br>Support_team</td></tr>
    <tr><td class="id"><i></i><u>1592</u></td><td>2</td><td>None</td><td>7</td><td>Feedback<br>([VexTal] Support_team)</td><td>New Feature<br>Request</td><td>Editor os estilos do treeview do<br>Volteq atual co..</td><td>2014 - 12 - 03 15:59:54</td><td>[VexTal]<br>Support_team</td></tr>
    <tr><td class="id"><i></i><u>1592</u></td><td>2</td><td>None</td><td>7</td><td>Feedback<br>([VexTal] Support_team)</td><td>New Feature<br>Request</td><td>Editor os estilos do treeview do<br>Volteq atual co..</td><td>2014 - 12 - 03 15:59:54</td><td>[VexTal]<br>Support_team</td></tr>
    <tr><td class="id"><i></i><u>1592</u></td><td>2</td><td>None</td><td>7</td><td>Feedback<br>([VexTal] Support_team)</td><td>New Feature<br>Request</td><td>Editor os estilos do treeview do<br>Volteq atual co..</td><td>2014 - 12 - 03 15:59:54</td><td>[VexTal]<br>Support_team</td></tr>
    <tr><td class="id"><i></i><u>1592</u></td><td>2</td><td>None</td><td>7</td><td>Feedback<br>([VexTal] Support_team)</td><td>New Feature<br>Request</td><td>Editor os estilos do treeview do<br>Volteq atual co..</td><td>2014 - 12 - 03 15:59:54</td><td>[VexTal]<br>Support_team</td></tr>
    <tr><td class="id"><i></i><u>1592</u></td><td>2</td><td>None</td><td>7</td><td>Feedback<br>([VexTal] Support_team)</td><td>New Feature<br>Request</td><td>Editor os estilos do treeview do<br>Volteq atual co..</td><td>2014 - 12 - 03 15:59:54</td><td>[VexTal]<br>Support_team</td></tr>
    <tr><td class="id"><i></i><u>1592</u></td><td>2</td><td>None</td><td>7</td><td>Feedback<br>([VexTal] Support_team)</td><td>New Feature<br>Request</td><td>Editor os estilos do treeview do<br>Volteq atual co..</td><td>2014 - 12 - 03 15:59:54</td><td>[VexTal]<br>Support_team</td></tr>
    <tr><td class="id"><i></i><u>1592</u></td><td>2</td><td>None</td><td>7</td><td>Feedback<br>([VexTal] Support_team)</td><td>New Feature<br>Request</td><td>Editor os estilos do treeview do<br>Volteq atual co..</td><td>2014 - 12 - 03 15:59:54</td><td>[VexTal]<br>Support_team</td></tr>
    <tr><td class="id"><i></i><u>1592</u></td><td>2</td><td>None</td><td>7</td><td>Feedback<br>([VexTal] Support_team)</td><td>New Feature<br>Request</td><td>Editor os estilos do treeview do<br>Volteq atual co..</td><td>2014 - 12 - 03 15:59:54</td><td>[VexTal]<br>Support_team</td></tr>
  </tbody>
</table>

<div class="pager"><span>1</span><span>2</span><span>3</span><span>4</span><span>5</span><span>6</span><span>7</span><span>8</span><span>9</span><span style="margin-left:14px">&gt;</span><span style="margin-left:22px">&gt;&gt;</span></div>

<div class="bulk">
  <span class="check"></span><span style="font-size:9.5px">Select all</span>
  <div class="select" style="width:116px;margin-left:19px">Update Priority</div>
  <div class="select" style="width:116px;margin-left:9px">None</div>
  <div class="go">Go</div>
</div>

<div class="legend">
  <span style="background:#f7a9ab">open</span>
  <span style="background:#c9c5f2">assigned</span>
  <span style="background:#f36f6f">feedback</span>
  <span style="background:#f7d64a">acknowledged</span>
  <span style="background:#faf2a8">confirmed</span>
  <span style="background:#c8ecd4">resolved</span>
  <span style="background:#e3e3e3">closed</span>
</div>

<div class="chartbar">
  <span style="color:#e46b6b;margin:0 12px 0 3px">✕ +</span>Chart - DL MCS TBs
  <span style="border-left:1px solid #aaa;height:17px;margin:0 12px 0 14px"></span>
  <span class="pill">DY</span><span style="margin-left:12px">◎Options</span>
  <span style="margin-left:14px">From:</span><span class="pill">2014-03-30</span>
  <span>To:</span><span class="pill">2014-03-30</span><span class="pill" style="margin-left:2px">GO</span>
</div>
<div class="chartbox"></div>

<footer class="footer">
  <div class="flinks"><span>Home</span><span>|</span><span>About Us</span><span>|</span><span>Service</span><span>|</span><span>Contact</span></div>
  <div class="frule"></div>
  <div class="copy">Yoursite © 2014 All Rights Reserved.</div>
  <div class="social"><i></i><i></i><i></i></div>
  <div class="tag">M3</div>
</footer>
</body>
</html>
```